Technology management company looking for a new website with a professional look

Brennick IT is a recently re-branded technology management company that is looking for a website design to match its personalized approach and friendly culture.

We would like to see a specialized, but related, page style for each of our main service offerings of:

• Commercial IT Support (This is our primary focus)
• Commercial Phone Systems (We partner with http://www.voxtrell.com/ for our phone systems)
• Point of Sale Systems (We partner with http://www.tillmora.com/ for our POS systems.
• Web Design
• Hollow Pine Computers (Our residential computer service offering, branded as Hollow Pine Computers)

The Hollow Pine Computers page should be build upon the Hollow Pine Computers logo, the other four pages should be branded as Brennick IT.

These five separate pages should have subtle, yet clearly defined links to one another. They should also each have a Home, Products, Service, and Company in the menu.

The website should have a clean design with professional appeal, but not appear too sterile or uninviting. It needs to have a simple, easy to navigate menu interface along the top. We would also like the site to be mobile friendly.

It should also allow us to easily tie in links to our social media pages (Facebook, LinkedIn, Twitter and Google+) and provide easy access to our contact information from each page.

This is a link to our old website www.hollowpinecomputers.com

We don't currently have copy available. The text and menu design should be easily editable and expandable so we can use the design to fit our copy.

In general we are looking for a concept we can modify to fit our needs.

We need this design to be available with layers in a .psd format.

Target Market(s)

Small to mid-size businesses.

Industry/Entity Type

Information Technology

Number of Pages Required

5+ page

Font styles to use
Sans Serif

Requirements
Must have
• Mobile Friendly
• Professional Type Face
• Unity between all pages
• .PSD Format
Nice to have
• Themed with our logo
Should not have
• Bubbly unprofessional typeface. No comic sans.

```html
<!DOCTYPE html>
<html lang="en">
<head>
<meta charset="utf-8">
<title>Brennick IT – Technology Management</title>
<link href="https://fonts.googleapis.com/css2?family=Open+Sans:wght@400;600;700&display=swap" rel="stylesheet">
<style>
:root{
  --orange:#f26522;
  --ink:#222222;
  --text:#666666;
  --muted:#999999;
  --line:#dddddd;
  --panel:#f3f3f3;
  --footer:#1f1f1f;
  --footer-text:#8a8a8a;
  --white:#ffffff;
}
*{box-sizing:border-box;margin:0;padding:0}
html,body{width:784px;height:1200px;overflow:hidden}
body{font-family:"Open Sans",Arial,sans-serif;background:var(--white);color:var(--text);position:relative}

/* header */
.site-header{position:absolute;top:0;left:0;width:784px;height:57px;background:var(--white);border-bottom:1px solid var(--line)}
.brand{position:absolute;left:24px;top:16px;font-weight:700;font-size:20px;line-height:24px;color:var(--ink)}
.main-nav{position:absolute;right:20px;top:0;display:flex;height:57px}
.main-nav a{display:block;padding:0 13px;font-size:10px;font-weight:600;color:var(--ink);text-decoration:none;text-transform:uppercase;border-top:3px solid transparent;line-height:51px}
.main-nav a.active{color:var(--orange);border-top-color:var(--orange)}

/* hero */
.hero{position:absolute;top:57px;left:0;width:784px;height:323px;background:linear-gradient(90deg,#f2f2f2 0%,#e6e6e6 55%,#d8d8d8 100%);overflow:hidden}
.hero-photo{position:absolute;right:0;top:0;width:340px;height:323px;background:linear-gradient(180deg,#d9cfc6 0%,#c9b6a6 45%,#e9e4df 100%)}
.hero-card{position:absolute;left:72px;top:180px;width:300px;height:130px;background:rgba(40,40,40,.85);padding:12px 16px}
.hero-kicker{color:var(--white);font-size:17px;font-weight:400;line-height:22px}
.hero-title{color:var(--orange);font-size:36px;font-weight:700;line-height:42px}
.btn{display:inline-block;background:var(--orange);color:var(--white);font-size:9px;font-weight:600;text-transform:uppercase;padding:8px 12px;border-radius:2px;text-decoration:none}
.hero-card .btn{margin-top:8px}
.hero-dots{position:absolute;left:84px;top:296px;display:flex;gap:6px}
.hero-dots span{width:7px;height:7px;border-radius:50%;background:#bbb}
.hero-dots span.on{background:var(--white)}

/* services */
.services{position:absolute;top:380px;left:0;width:784px;height:313px}
.service{position:absolute;width:200px;text-align:center}
.service svg{width:40px;height:40px;stroke:#777;fill:none;stroke-width:2.2}
.service h3{color:var(--orange);font-size:16px;font-weight:400;margin-top:8px}
.service p{font-size:8px;line-height:1.5;color:var(--muted);margin:6px auto 0;width:160px}

/* welcome + callback */
.intro{position:absolute;top:693px;left:0;width:784px;height:261px;background:var(--panel)}
.welcome{position:absolute;left:62px;top:36px;width:290px}
.intro h2{font-size:21px;font-weight:600;color:var(--ink)}
.intro h2 span{color:var(--orange)}
.welcome p{font-size:8px;line-height:1.6;color:var(--muted);margin-top:14px}
.welcome .btn{margin-top:18px;background:var(--ink)}
.callback{position:absolute;left:384px;top:36px;width:340px}
.field-row{display:flex;gap:12px;margin-top:16px}
.field{flex:1;height:30px;background:var(--white);border:1px solid var(--line);font-size:8px;color:var(--muted);padding:9px 10px}
.field.message{height:64px;margin-top:10px}
.callback .btn{margin-top:14px;background:var(--ink)}

/* partners */
.partners{position:absolute;top:954px;left:0;width:784px;height:188px;background:var(--orange)}
.partners h2{text-align:center;color:var(--white);font-size:22px;font-weight:400;margin-top:36px}
.partner-badge{position:absolute;top:91px;height:65px;background:var(--white);border-radius:2px}

/* footer */
.site-footer{position:absolute;top:1142px;left:0;width:784px;height:58px;background:var(--footer)}
.footer-links{position:absolute;left:62px;top:14px;display:flex;gap:6px;font-size:8px;color:var(--footer-text)}
.copyright{position:absolute;left:62px;top:32px;font-size:8px;color:var(--footer-text)}
.social{position:absolute;right:60px;top:18px;display:flex;gap:6px}
.social span{width:18px;height:18px;background:#3a3a3a;border-radius:2px}
.to-top{position:absolute;right:16px;top:22px;font-size:8px;color:var(--footer-text);font-weight:700}
</style>
</head>
<body>

<header class="site-header">
  <div class="brand">Brennick IT</div>
  <nav class="main-nav">
    <a href="#" class="active">Home</a>
    <a href="#">About us</a>
    <a href="#">Services</a>
    <a href="#">Testimonials</a>
    <a href="#">Blog</a>
    <a href="#">Contact</a>
  </nav>
</header>

<section class="hero" role="img" aria-label="Light grey backdrop with hand-sketched technology doodles">
  <div class="hero-photo" role="img" aria-label="Photo of a thoughtful businessman looking up"></div>
  <div class="hero-card">
    <div class="hero-kicker">Commercial</div>
    <div class="hero-title">IT Support</div>
    <a href="#" class="btn">Read more</a>
  </div>
  <div class="hero-dots"><span class="on"></span><span></span><span></span></div>
</section>

<section class="services">
  <div class="service" style="left:67px;top:40px">
    <svg viewBox="0 0 40 40"><rect x="5" y="12" width="30" height="22" rx="2"/><path d="M14 12V7h12v5M5 21h30"/></svg>
    <h3>IT Support</h3>
    <p>Proactive monitoring and fast help desk support that keeps your whole office running.</p>
  </div>
  <div class="service" style="left:297px;top:40px">
    <svg viewBox="0 0 40 40"><rect x="12" y="4" width="16" height="32" rx="3"/><path d="M18 31h4"/></svg>
    <h3>Phone Systems</h3>
    <p>Modern business phone systems set up, managed and supported by our local team.</p>
  </div>
  <div class="service" style="left:540px;top:40px">
    <svg viewBox="0 0 40 40"><path d="M6 36V14h10v22M16 36V5h18v31M4 36h32"/><path d="M21 10h3M27 10h3M21 16h3M27 16h3M21 22h3M27 22h3M10 19h2M10 25h2"/></svg>
    <h3>Sale Systems</h3>
    <p>Point of sale systems fitted to your store, with training and ongoing care.</p>
  </div>
  <div class="service" style="left:187px;top:170px">
    <svg viewBox="0 0 40 40"><rect x="4" y="6" width="32" height="22" rx="1"/><path d="M16 28l-2 6h12l-2-6M12 34h16"/></svg>
    <h3>Web Design</h3>
    <p>Clean, mobile friendly websites that tell your story and bring customers in.</p>
  </div>
  <div class="service" style="left:415px;top:170px">
    <svg viewBox="0 0 40 40"><path d="M6 16h8l16-9v26l-16-9H6z"/><path d="M10 24l3 10h4l-2-10"/></svg>
    <h3>Hollow Pine</h3>
    <p>Friendly home computer repair, cleanup and setup for families across the valley.</p>
  </div>
</section>

<section class="intro">
  <div class="welcome">
    <h2>Welcome to <span>Brennick IT</span></h2>
    <p>We are a technology management company with a personal approach. Our friendly team looks after the computers, networks and phones of small and mid-size businesses, so you can focus on your own work.</p>
    <p>From a single workstation to a whole office, we plan, install and support the tools you rely on, and we answer when you call.</p>
    <a href="#" class="btn">Read more</a>
  </div>
  <div class="callback">
    <h2>Request a <span>Free Callback</span></h2>
    <div class="field-row">
      <div class="field">Name</div>
      <div class="field">Phone Number</div>
    </div>
    <div class="field message">Message</div>
    <a href="#" class="btn">Submit</a>
  </div>
</section>

<section class="partners">
  <h2>Our partners</h2>
  <div class="partner-badge" style="left:162px;width:144px"></div>
  <div class="partner-badge" style="left:327px;width:138px"></div>
  <div class="partner-badge" style="left:486px;width:141px"></div>
</section>

<footer class="site-footer">
  <div class="footer-links"><span>Home</span>|<span>About us</span>|<span>Services</span>|<span>Testimonials</span>|<span>Blog</span>|<span>Contact</span></div>
  <div class="copyright">Copyright © 2013</div>
  <div class="social"><span></span><span></span><span></span><span></span></div>
  <div class="to-top">UP</div>
</footer>

</body>
</html>
```